Providing Back Office Solutions to Financial Advisors and Attorney Needs a Business Card Design

Need a Business Card Design that speaks to Financial Advisor and Attorneys. Some of the word that come to mind is Clean/Simple & Futuristic.

Industry/Entity Type

Business

```html
<!DOCTYPE html>
<html lang="en">
<head>
<meta charset="utf-8">
<title>Cardina Back Office Solutions – Business Card</title>
<link rel="stylesheet" href="https://fonts.googleapis.com/css2?family=Montserrat:wght@400;500;600&display=swap">
<style>
  :root {
    --page: #e9eaec;
    --card: #ffffff;
    --brand-blue: #1d7fc0;
    --brand-blue-soft: #3f8fd0;
    --ink: #3a3c40;
    --icon: #1d6fb0;
  }
  * { margin: 0; padding: 0; box-sizing: border-box; }
  html, body {
    width: 1200px; height: 900px; overflow: hidden;
    background: var(--page);
    font-family: "Montserrat", sans-serif;
  }
  .business-card {
    position: absolute; left: 100px; top: 164px;
    width: 1000px; height: 572px;
    background: var(--card);
    box-shadow: 0 18px 40px rgba(0,0,0,0.12), 0 2px 6px rgba(0,0,0,0.08);
  }
  .brand {
    position: absolute; left: 150px; top: 92px;
    display: flex; align-items: center; gap: 26px;
  }
  .brand-square {
    width: 78px; height: 78px; background: var(--brand-blue);
  }
  .brand-divider {
    width: 2px; height: 118px; background: var(--brand-blue);
  }
  .brand-name {
    font-size: 66px; font-weight: 500; letter-spacing: 4px;
    color: var(--brand-blue); line-height: 1;
  }
  .brand-tagline {
    margin-top: 10px;
    font-size: 21px; font-weight: 400; letter-spacing: 1px;
    color: var(--brand-blue-soft);
  }
  .contact-list {
    position: absolute; left: 90px; top: 318px;
    list-style: none;
  }
  .contact-item {
    display: flex; align-items: center; gap: 14px;
    font-size: 24px; color: var(--ink); line-height: 38px;
  }
  .contact-item svg { width: 22px; height: 22px; flex: none; }
  .person {
    position: absolute; right: 80px; top: 222px; text-align: right;
  }
  .person-name {
    font-size: 50px; font-weight: 600; color: var(--brand-blue); line-height: 1.1;
  }
  .person-title {
    font-size: 32px; font-weight: 400; color: var(--ink);
  }
  .address {
    position: absolute; right: 80px; bottom: 60px; text-align: right;
    font-size: 24px; color: var(--ink); line-height: 34px; font-style: normal;
  }
</style>
</head>
<body>
  <section class="business-card">
    <div class="brand">
      <div class="brand-square"></div>
      <div class="brand-divider"></div>
      <div class="brand-text">
        <div class="brand-name">CARDINA</div>
        <div class="brand-tagline">BACK OFFICE SOLUTIONS</div>
      </div>
    </div>

    <ul class="contact-list">
      <li class="contact-item">
        <svg viewBox="0 0 24 24" aria-hidden="true"><path fill="var(--icon)" d="M6.6 10.8c1.4 2.8 3.8 5.1 6.6 6.6l2.2-2.2c.3-.3.7-.4 1-.2 1.1.4 2.3.6 3.6.6.6 0 1 .4 1 1V20c0 .6-.4 1-1 1C10.6 21 3 13.4 3 4c0-.6.4-1 1-1h3.5c.6 0 1 .4 1 1 0 1.3.2 2.5.6 3.6.1.3 0 .7-.2 1L6.6 10.8z"/></svg>
        555 210 4471
      </li>
      <li class="contact-item">
        <svg viewBox="0 0 24 24" aria-hidden="true"><rect x="6" y="2" width="12" height="20" rx="2" fill="none" stroke="var(--icon)" stroke-width="2"/><circle cx="12" cy="18" r="1.2" fill="var(--icon)"/></svg>
        555 382 9016
      </li>
      <li class="contact-item">
        <svg viewBox="0 0 24 24" aria-hidden="true"><rect x="2" y="5" width="20" height="14" rx="1" fill="var(--icon)"/><path d="M2.5 6l9.5 7 9.5-7" fill="none" stroke="#fff" stroke-width="1.6"/></svg>
        info@cardinabos.com
      </li>
      <li class="contact-item">
        <svg viewBox="0 0 24 24" aria-hidden="true"><g fill="none" stroke="var(--icon)" stroke-width="1.8"><circle cx="12" cy="12" r="9.5"/><ellipse cx="12" cy="12" rx="4.5" ry="9.5"/><path d="M2.5 12h19M4 7h16M4 17h16"/></g></svg>
        www.cardinabos.com
      </li>
    </ul>

    <div class="person">
      <div class="person-name">Daniel Hart</div>
      <div class="person-title">President</div>
    </div>

    <address class="address">
      42 Linden Park Road<br>
      Fairbourne 3100
    </address>
  </section>
</body>
</html>
```